Design website for new email startup

We are starting a company called Ravo.QT (it will live at http://ravo.qt.example).

We would like the main landing page for our site designed. We have provided a very simple wireframe to help provide direction for the content it should include, but we do not expect the designers to adhere to it at all - we encourage unique ideas. There is some sample text in the wireframe - this does not have to be used, but may provide ideas.

We provide an easy way for people to manage email for a custom domain name. For example if you own "myhomeplace.example" you can point your DNS records to us and we'll make it easy to have emails addressed to your domain get forwarded to your existing email (gmail, etc). Folks running blogs, and other small sites can quickly setup email addresses for their domains and manage them in one place.

(For technical folks, we have you point your dns mx records to us, hence the name. That way all your email hits us and we can redirect it wherever you want. We make it easy to manage a single domain or a bunch of domains. Many domain registrars offer this service for a fee, and have clumsy management tools. We provide a robust simple toolset for free, as well as premium options).

The goal of the landing page is to get folks into the signup flow. The second priority flow is to have them take a look at the premium plan offerings.

We may offer the winning designer additional work for the remainder of the site design.
Updates

I've changed this project to a committed payment.  It is no longer refundable.  Thank you.

Target Market(s)

Bloggers, podcasters, designers, app developers - people who are a little tech savvy.

Industry/Entity Type

It Company

Font styles to use
Sans Serif

Colors

Designer to choose colors to be used in the design.

Requirements
Must have
• A full fidelity mockup (comp) of the landing page including the source file (psd, ai, etc).

Some sort of logo treatment for the ravo.qt brand

A call to action for signup, such as the suggested 'Get Started Here'
Nice to have
• A hip startup feel

Incorporation of the email theme

Give the impression it is simple, easy and fast

```html
<!DOCTYPE html>
<html lang="en">
<head>
<meta charset="utf-8">
<title>Ravo.QT — We Make Email Easy</title>
<link href="https://fonts.googleapis.com/css2?family=Open+Sans:wght@400;600;700&family=PT+Sans+Narrow:wght@400;700&display=swap" rel="stylesheet">
<style>
  :root {
    --header-bg: #1c1c1c;
    --teal: #1ba3ad;
    --teal-deep: #0f8f99;
    --blue: #3a8fca;
    --blue-dark: #2a72ad;
    --salmon: #ee8a6c;
    --orange: #f2a94a;
    --ink: #1e1e1e;
    --slate: #454545;
    --slate-dark: #2f2f2f;
    --footer-bg: #3f3f3f;
    --white: #ffffff;
    --nav-text: #d8d8d8;
  }
  * { box-sizing: border-box; margin: 0; padding: 0; }
  html, body { width: 1200px; height: 850px; overflow: hidden; }
  body { position: relative; font-family: "Open Sans", Arial, sans-serif; background: var(--white); }

  .site-header { position: absolute; left: 0; top: 0; width: 1200px; height: 75px; background: var(--header-bg); }
  .brand { position: absolute; left: 198px; top: 12px; font-family: "Open Sans", sans-serif; font-weight: 600; font-size: 34px; letter-spacing: -1px; color: var(--teal); }
  .main-nav a { position: absolute; top: 47px; width: 64px; height: 28px; text-align: center; font-family: "PT Sans Narrow", sans-serif; font-size: 13px; color: var(--nav-text); text-decoration: none; }
  .main-nav a::after { content: ""; position: absolute; left: 0; bottom: 0; width: 64px; height: 5px; }
  .nav-how { left: 804px; } .nav-how::after { background: var(--blue); }
  .nav-support { left: 870px; } .nav-support::after { background: var(--orange); }
  .nav-login { left: 937px; } .nav-login::after { background: var(--salmon); }

  .hero { position: absolute; left: 0; top: 75px; width: 1200px; height: 487px;
    background: linear-gradient(to bottom, #27b5bf 0%, #8ed7dc 12%, #ffffff 30%, #ffffff 68%, #8ed7dc 86%, #1a9ea8 100%); }
  .hero-title { position: absolute; left: 0; top: 121px; width: 1200px; text-align: center; font-family: "PT Sans Narrow", sans-serif; font-weight: 700; font-size: 56px; letter-spacing: -1px; line-height: 70px; }
  .hero-title .we { color: var(--salmon); }
  .hero-title .mid { color: var(--blue); }
  .hero-title .easy { color: var(--orange); }
  .hero-lines { position: absolute; left: 0; top: 191px; width: 1230px; text-align: center; font-family: "PT Sans Narrow", sans-serif; font-size: 18px; line-height: 28px; color: var(--ink); }

  .cta { position: absolute; top: 326px; width: 343px; height: 49px; border-radius: 4px; text-align: center; line-height: 49px; font-weight: 700; font-size: 28px; color: var(--white); text-decoration: none; letter-spacing: -0.5px; }
  .cta-start { left: 199px; background: linear-gradient(var(--blue), var(--blue-dark)); border: 1px solid #2b6fa5; }
  .cta-plans { left: 658px; top: 328px; background: linear-gradient(var(--slate), var(--slate-dark)); border: 1px solid #222; }
  .cta-or { position: absolute; left: 562px; top: 327px; width: 60px; text-align: center; font-weight: 700; font-size: 38px; line-height: 46px; color: var(--ink); }

  .partners { position: absolute; left: 0; top: 562px; width: 1200px; height: 226px; background: var(--blue); color: var(--white); }
  .partners .divider { position: absolute; left: 600px; top: 30px; width: 1px; height: 154px; background: #2b5f85; }
  .partner { position: absolute; top: 16px; width: 340px; text-align: center; }
  .partner-left { left: 229px; } .partner-right { left: 629px; }
  .partner h2 { font-size: 14px; font-weight: 600; line-height: 17px; letter-spacing: 0.3px; height: 40px; }
  .partner .mark { height: 104px; display: flex; align-items: center; justify-content: center; gap: 10px; font-weight: 700; font-size: 32px; color: var(--white); }
  .partner .mark span.dot { width: 26px; height: 26px; border-radius: 50%; background: var(--orange); }
  .partner .more { display: block; margin-top: 33px; font-size: 12px; color: var(--white); text-decoration: none; }

  .site-footer { position: absolute; left: 0; top: 790px; width: 1200px; height: 60px; background: var(--footer-bg); border-top: 2px solid var(--white); text-align: center; line-height: 56px; font-size: 12px; color: var(--white); }
</style>
</head>
<body>
  <header class="site-header">
    <div class="brand">Ravo.QT</div>
    <nav class="main-nav">
      <a class="nav-how" href="#">How It Works</a>
      <a class="nav-support" href="#">Support</a>
      <a class="nav-login" href="#">Login</a>
    </nav>
  </header>

  <section class="hero" role="img" aria-label="Teal pixel mosaic fading into white, evoking falling email bits">
    <h1 class="hero-title"><span class="we">WE</span> <span class="mid">MAKE EMAIL</span> <span class="easy">EASY</span></h1>
    <p class="hero-lines">Give Us Five Minutes And We’ll Get You Email Form Your Domain<br>Easily Forward Mail Form Your Custom Domain Name Wherever You Want It<br>You Take The Mail, We’ll Keep The Spam</p>
    <a class="cta cta-start" href="#">GET STARTED HERE</a>
    <div class="cta-or">OR</div>
    <a class="cta cta-plans" href="#">COMPARE PLANS</a>
  </section>

  <section class="partners">
    <div class="divider"></div>
    <article class="partner partner-left">
      <h2>How to configure your SkyVeil DNS to use<br>RAVO.QT</h2>
      <div class="mark"><span class="dot"></span>SkyVeil</div>
      <a class="more" href="#">READMORE</a>
    </article>
    <article class="partner partner-right">
      <h2>Use ravo with your DomainPeak domain<br>registration for reliable email forwarding</h2>
      <div class="mark">DomainPeak</div>
      <a class="more" href="#">READMORE</a>
    </article>
  </section>

  <footer class="site-footer">Copyright 2014 &nbsp;Ravo.QT &nbsp;|&nbsp; All Rights Reserved &nbsp;|&nbsp; Powered by Ravo.QT</footer>
</body>
</html>
```